IT services company requires Letterhead design

We need a professional letterhead designed to be used for general correspondence with customers, quotes, invoices etc. We are a new IT services company specialising in computer servicing and repairs and mobile and tablet repairs. Attached are templates that my printing company have supplied, my logos, an interpretation of our website for you to get a feel of the company. Details to be included on the letterhead are

Company Number – 4738261
VAT Number - 518337942
Registered Address – 14-16 Brambly Lane, London, E4 9QT

Phone – 01632 487215
Email – sales@quorvent.com
Web – www.quorvent.com

I would prefer for the top of the letterhead to just have the company logo on a white background and the rest of the details on the bottom of the letterhead but I am open to design ideas.

Thanks

```html
<!DOCTYPE html>
<html lang="en">
<head>
<meta charset="utf-8">
<title>Quorvent Letterhead</title>
<link href="https://fonts.googleapis.com/css2?family=Ubuntu:wght@400;500;700&display=swap" rel="stylesheet">
<style>
  :root {
    --backdrop: #b3b4b6;
    --paper: #ffffff;
    --brand-cyan: #2bc3e1;
    --brand-dark: #33363a;
    --watermark: #f4f4f4;
    --footer-text: #ffffff;
  }
  * { box-sizing: border-box; margin: 0; padding: 0; }
  html, body {
    width: 927px; height: 1200px; overflow: hidden;
    background: var(--backdrop);
    font-family: "Ubuntu", Arial, sans-serif;
  }
  .sheet {
    position: absolute; left: 91px; top: 73px;
    width: 746px; height: 1054px;
    background: var(--paper);
    overflow: hidden;
  }
  .masthead {
    position: absolute; top: 38px; left: 0; width: 100%;
    display: flex; justify-content: center; align-items: center; gap: 10px;
  }
  .masthead .mark-square {
    width: 16px; height: 16px; background: var(--brand-cyan);
  }
  .masthead .brand-name {
    font-size: 34px; font-weight: 700; color: var(--brand-dark);
    letter-spacing: 0.5px;
  }
  .watermark-name {
    position: absolute; top: 500px; left: 0; width: 100%;
    text-align: center;
    font-size: 130px; font-weight: 700; color: var(--watermark);
    line-height: 1;
  }
  .footer-band {
    position: absolute; left: 0; bottom: 0;
    width: 100%; height: 72px;
    background: var(--brand-cyan);
    color: var(--footer-text);
    font-size: 11px;
  }
  .footer-band .notch {
    position: absolute; left: 17px; top: 0;
    width: 36px; height: 15px;
  }
  .footer-brand {
    position: absolute; left: 34px; top: 0; height: 100%;
    display: flex; align-items: center;
    font-size: 12.5px; font-weight: 500;
  }
  .divider {
    position: absolute; top: 22px; width: 2px; height: 36px;
    background: var(--footer-text);
  }
  .divider.first { left: 109px; }
  .divider.second { left: 294px; }
  .info-line {
    position: absolute; white-space: nowrap;
    display: flex; align-items: center; gap: 3px;
    line-height: 1;
  }
  .row-top { top: 27px; }
  .row-bottom { top: 45px; }
  .info-line svg { width: 11px; height: 11px; fill: var(--footer-text); }
  .sep { position: absolute; top: 45px; line-height: 1; }
</style>
</head>
<body>
  <div class="sheet">
    <header class="masthead">
      <span class="mark-square"></span>
      <span class="brand-name">Quorvent</span>
    </header>

    <div class="watermark-name" aria-hidden="true">Quorvent</div>

    <footer class="footer-band">
      <svg class="notch" viewBox="0 0 36 15" aria-hidden="true"><polygon points="0,0 36,0 18,15" fill="#ffffff"/></svg>
      <div class="footer-brand">Quorvent</div>
      <span class="divider first"></span>

      <div class="info-line row-top" style="left:120px">Company Number:&nbsp; 4738261</div>
      <div class="info-line row-bottom" style="left:120px">VAT Number:&nbsp; 518337942</div>

      <span class="divider second"></span>

      <div class="info-line row-top" style="left:305px">
        <svg viewBox="0 0 24 24"><path d="M12 1a8 8 0 0 0-8 8c0 6 8 14 8 14s8-8 8-14a8 8 0 0 0-8-8zm0 11a3 3 0 1 1 0-6 3 3 0 0 1 0 6z"/></svg>
        14-16 Brambly Lane, London, E4 9QT
      </div>
      <div class="info-line row-bottom" style="left:305px">
        <svg viewBox="0 0 24 24"><path d="M6.6 10.8a15 15 0 0 0 6.6 6.6l2.2-2.2a1 1 0 0 1 1-.25 11.4 11.4 0 0 0 3.6.57 1 1 0 0 1 1 1V20a1 1 0 0 1-1 1A17 17 0 0 1 3 4a1 1 0 0 1 1-1h3.5a1 1 0 0 1 1 1c0 1.25.2 2.45.57 3.57a1 1 0 0 1-.25 1z"/></svg>
        01632&nbsp; 487215
      </div>
      <span class="sep" style="left:421px">|</span>
      <div class="info-line row-bottom" style="left:451px">
        <svg viewBox="0 0 24 24"><path d="M2 5h20v14H2zm2 2v.5l8 5 8-5V7zm0 2.8V17h16V9.8l-8 5z"/></svg>
        sales@quorvent.com
      </div>
      <span class="sep" style="left:585px">|</span>
      <div class="info-line row-bottom" style="left:614px">
        <svg viewBox="0 0 24 24"><path d="M12 2a10 10 0 1 0 0 20 10 10 0 0 0 0-20zm6.9 6h-2.9a15 15 0 0 0-1.4-3.6A8 8 0 0 1 18.9 8zM12 4c.8 1.2 1.5 2.5 1.9 4h-3.8c.4-1.5 1.1-2.8 1.9-4zM4.3 14a8 8 0 0 1 0-4h3.4a16 16 0 0 0 0 4zm.8 2h2.9a15 15 0 0 0 1.4 3.6A8 8 0 0 1 5.1 16zM8 8H5.1a8 8 0 0 1 4.3-3.6A15 15 0 0 0 8 8zm4 12c-.8-1.2-1.5-2.5-1.9-4h3.8c-.4 1.5-1.1 2.8-1.9 4zm2.3-6H9.7a14 14 0 0 1 0-4h4.6a14 14 0 0 1 0 4zm.3 5.6A15 15 0 0 0 16 16h2.9a8 8 0 0 1-4.3 3.6zm1.7-5.6a16 16 0 0 0 0-4h3.4a8 8 0 0 1 0 4z"/></svg>
        www.quorvent.com
      </div>
    </footer>
  </div>
</body>
</html>
```